Revise our Visual Graphic - CPA firm

We are a small specialty CPA firm that provides consulting services to companies in three areas: Information Security, Compliance & Attestation.

We need a tool to present our range of services and how they help our customers. We might use this on the website and when meeting face to face with clients to talk through what we do and how we can help.

I'm seeking a revised and updated graphic presentation image to explain our services. This graphic framework image will be one we can use on our website and use when we sell and explain our services to our clients. This graphic framework is meant to be a visual tool to make is easier to explain what we do to our clients.

We have a graphic that we like, but we don't LOVE IT yet. Your mission is you choose to accept it is to professionalize our graphic design. (see attached graphic)

The overall "environment" is represented by RISK, REGULATORY, REVENUE. These are the 3 reasons people would hire us. The bigger picture eco system.

The three overlapping circles show are three major service categories and inside the circles are lists of the specific services we can provide. We have overlapping circles to show that we can save them money and time if we provide more than one type of service.

The words on the dotted lines are what we commonly do on each project which is 3 things: IDENTIFY, EVALUATE, REPORT. These three things we do for all of our services so a faint circle with arrows or somehow showing a circular ongoing process would be good.

As you can see we are using one graphic to show many things and relationships.

The title of this graphic is "T5 Framework"

I look forward to your great ideas! Thanks.

Reason: Just to give a little more time after the weekend.

Target Market(s)

Presidents and Vice Presidents of small companies.

Industry/Entity Type

Graphic Design

Colors
faee3f
86cfc7
acd037
f68d4d

Requirements
Must have
• Be able to show this visual on one page of a website or PowerPoint presentation without scrolling down.

All of the written text on my draft example must be used and fit into the new design.
Nice to have
• When you design it think of how this can be used for both presentations, but also may be used on the website and people might click on different elements to learn more.

I picked some colors, but feel free to pick other colors. The only important thing to know is that the logo is black and yellow.

```html
<!DOCTYPE html>
<html lang="en">
<head>
<meta charset="utf-8">
<title>T5 Framework</title>
<link rel="stylesheet" href="https://fonts.googleapis.com/css2?family=Montserrat:wght@600;700&family=Raleway:wght@300;400&display=swap">
<style>
  :root {
    --bg: #f1f1f1;
    --ring: #e4e4e6;
    --triangle: #94c6db;
    --circle: rgba(60, 138, 190, 0.42);
    --core: #f4ec68;
    --corner: #f6996a;
    --corner-letter: #f6e85f;
    --driver: #f5925c;
    --process: #a8d48f;
    --label: #6a6f73;
    --service: #f3f7fa;
    --title-bg: #92c5d8;
    --title-text: #ffffff;
  }
  * { margin: 0; padding: 0; box-sizing: border-box; }
  html, body { width: 1200px; height: 1000px; overflow: hidden; background: var(--bg); }
  .framework { display: block; width: 1200px; height: 1000px; }
  .heading-badge { fill: var(--title-bg); }
  .heading-text { font-family: "Montserrat", sans-serif; font-weight: 700; font-size: 38px; fill: var(--title-text); letter-spacing: 1px; }
  .process-ring { fill: var(--ring); }
  .process-arc { fill: none; stroke: var(--process); stroke-width: 3; stroke-dasharray: 11 7; }
  .arrow-head { fill: var(--process); }
  .environment { fill: var(--triangle); }
  .corner { fill: var(--corner); }
  .corner-letter { font-family: "Montserrat", sans-serif; font-weight: 700; font-size: 36px; fill: var(--corner-letter); text-anchor: middle; }
  .driver { font-family: "Montserrat", sans-serif; font-weight: 600; font-size: 25px; fill: var(--driver); text-anchor: middle; letter-spacing: 0.5px; }
  .process-step { font-family: "Montserrat", sans-serif; font-weight: 700; font-size: 27px; fill: var(--process); text-anchor: middle; letter-spacing: 1px; }
  .service-area { fill: var(--circle); }
  .core { fill: var(--core); }
  .category { font-family: "Raleway", sans-serif; font-weight: 400; font-size: 18px; fill: var(--label); text-anchor: middle; letter-spacing: 0.5px; }
  .service { font-family: "Raleway", sans-serif; font-weight: 400; font-size: 14px; fill: var(--service); text-anchor: middle; }
  .firm-name { font-family: "Montserrat", sans-serif; font-weight: 700; font-size: 17px; fill: var(--driver); text-anchor: middle; }
</style>
</head>
<body>
<svg class="framework" viewBox="0 0 1200 1000" xmlns="http://www.w3.org/2000/svg" aria-label="T5 Framework diagram">
  <defs>
    <clipPath id="compliance-clip"><circle cx="528" cy="653" r="115"/></clipPath>
    <clipPath id="attestation-clip"><circle cx="672" cy="653" r="115"/></clipPath>
    <marker id="process-arrow" viewBox="0 0 10 10" refX="6" refY="5" markerWidth="5" markerHeight="5" orient="auto">
      <path class="arrow-head" d="M0,0 L10,5 L0,10 z"/>
    </marker>
  </defs>

  <g class="heading">
    <rect class="heading-badge" x="398" y="76" width="404" height="61" rx="14"/>
    <text class="heading-text" x="600" y="121" text-anchor="middle">T5 FRAMEWORK</text>
  </g>

  <circle class="process-ring" cx="600" cy="640" r="322"/>

  <g class="process-cycle">
    <path class="process-arc" d="M525,340 A322,322 0 0 0 288,683" marker-end="url(#process-arrow)"/>
    <path class="process-arc" d="M905,683 A322,322 0 0 0 678,342" marker-end="url(#process-arrow)"/>
    <path class="process-arc" d="M383,843 A322,322 0 0 0 815,845" marker-end="url(#process-arrow)"/>
  </g>

  <polygon class="environment" points="599,230 186,843 1012,843"/>

  <g class="corners">
    <polygon class="corner" points="599,230 659,318 539,318"/>
    <polygon class="corner" points="186,843 288,843 245,755"/>
    <polygon class="corner" points="1012,843 912,843 955,755"/>
    <text class="corner-letter" x="599" y="307">R</text>
    <text class="corner-letter" x="236" y="832">R</text>
    <text class="corner-letter" x="961" y="832">R</text>
  </g>

  <g class="drivers">
    <text class="driver" x="599" y="213">REGULATORY</text>
    <text class="driver" x="215" y="881">RISK</text>
    <text class="driver" x="950" y="878">REVENUE</text>
  </g>

  <g class="process-steps">
    <text class="process-step" transform="translate(372,512) rotate(-57)">IDENTIFY</text>
    <text class="process-step" transform="translate(820,512) rotate(57)">EVALUATE</text>
    <text class="process-step" x="600" y="878">REPORT</text>
  </g>

  <text class="category" x="597" y="416">INFORMATION</text>
  <text class="category" x="597" y="440">SECURITY</text>
  <text class="category" transform="translate(395,725) rotate(60)">COMPLIANCE</text>
  <text class="category" transform="translate(805,722) rotate(-60)">ATTESTATION</text>

  <g class="service-areas">
    <circle class="service-area" cx="599" cy="541" r="114"/>
    <circle class="service-area" cx="528" cy="653" r="115"/>
    <circle class="service-area" cx="672" cy="653" r="115"/>
  </g>

  <g clip-path="url(#compliance-clip)">
    <g clip-path="url(#attestation-clip)">
      <circle class="core" cx="599" cy="541" r="114"/>
    </g>
  </g>

  <g class="services">
    <text class="service" x="599" y="492">ISO 27001</text>
    <text class="service" x="599" y="510">PCI-DSS</text>
    <text class="service" x="599" y="528">Penetration Test</text>

    <text class="service" x="466" y="621">CFPB</text>
    <text class="service" x="466" y="639">Readiness</text>
    <text class="service" x="466" y="657">FISMA</text>
    <text class="service" x="466" y="675">FedRamp</text>
    <text class="service" x="466" y="693">HITECH</text>
    <text class="service" x="466" y="711">HIPAA</text>

    <text class="service" x="716" y="672">SSAE 16</text>
    <text class="service" x="716" y="690">WebTrust</text>
    <text class="service" x="716" y="708">SOC 2</text>
  </g>

  <text class="firm-name" x="598" y="641">TAVLEN</text>
</svg>
</body>
</html>
```